Medical IT Business with New logo needs a fresh stationary design

First time on sketch Harbor; Thought I would give it a go.
This project is for business cards alone but we have loads of design work that needs to take place in the immediate future.

We provide IT services to the Medical Industry and value ourselves as offering a premium product to the market.

I am after a fresh, clean design using full colour 2 sided cards which includes our current colour palettes from our logo.

Card's must include:
- Logo
- Slogan
- Name
- Adress
- Email
- Phone
- Fax
- Mobile

Target Market(s)

Surgeons, High Profile Medical Personnel

Industry/Entity Type

Business

Fonts, CMYK Colours and Logo files attached.

Requirements
Must have
• Card's must include:
• - Logo
• - Slogan
• - Name
• - Adress
• - Email
• - Phone
• - Fax
• - Mobile
Nice to have
• Needs to incorporate our colour palette (attached CMYK colours)
Should not have
• Black backgrounds. Black text ok.

```html
<!DOCTYPE html>
<html lang="en">
<head>
<meta charset="utf-8">
<title>Pulsewise Systems – Business Card</title>
<link href="https://fonts.googleapis.com/css2?family=Montserrat:wght@500;700&family=Open+Sans:wght@400;600&display=swap" rel="stylesheet">
<style>
  :root {
    --backdrop: #bfbfbf;
    --card: #ffffff;
    --teal: #0d7aa6;
    --teal-dark: #0f6e9b;
    --sky: #5bc3e6;
    --pale: #c8e0f1;
    --mid-blue: #6aa9d7;
    --blue: #1a78c2;
    --navy: #163a6b;
    --lavender-grey: #a9aec8;
    --line: #a9adb3;
    --label: #1a6f95;
    --muted: #8a93a6;
  }
  * { margin: 0; padding: 0; box-sizing: border-box; }
  html, body { width: 1200px; height: 852px; overflow: hidden; }
  body {
    background: var(--backdrop);
    position: relative;
    font-family: "Montserrat", sans-serif;
  }
  .card {
    position: absolute;
    top: 289px;
    width: 448px;
    height: 272px;
    background: var(--card);
    border-radius: 14px;
    overflow: hidden;
  }
  .card--front { left: 134px; }
  .card--back { left: 612px; }
  .card-art { position: absolute; inset: 0; }

  .brand { position: absolute; display: flex; align-items: center; }
  .brand-dot { border-radius: 50%; background: var(--blue); flex: none; }
  .brand-name {
    color: var(--navy);
    font-weight: 700;
    line-height: 1;
    letter-spacing: 0.5px;
  }
  .brand-tagline {
    font-family: "Open Sans", sans-serif;
    color: var(--muted);
    display: block;
    white-space: nowrap;
  }

  .card--front .brand { left: 23px; top: 24px; }
  .card--front .brand-dot { width: 54px; height: 54px; margin-right: 5px; }
  .card--front .brand-name { font-size: 18px; }
  .card--front .brand-tagline { font-size: 7.5px; margin-top: 3px; }

  .holder { position: absolute; left: 23px; top: 105px; color: var(--label); }
  .holder-name { font-size: 15px; font-weight: 700; letter-spacing: 1px; }
  .holder-title { font-size: 9.5px; font-weight: 700; letter-spacing: 1px; margin-top: 1px; }

  .contact-label {
    position: absolute;
    right: 187px;
    font-size: 11.5px;
    font-weight: 500;
    letter-spacing: 1px;
    color: var(--label);
    text-align: right;
    line-height: 15px;
    white-space: nowrap;
  }

  .tagline-band {
    position: absolute;
    left: 0; top: 112px;
    width: 448px; height: 51px;
    background: var(--teal);
    color: #fff;
    font-family: "Open Sans", sans-serif;
    font-size: 15.5px;
    display: flex; align-items: center; justify-content: center;
  }
  .card--back .brand { left: 164px; top: 208px; }
  .card--back .brand-dot { width: 36px; height: 36px; margin-right: 3px; }
  .card--back .brand-name { font-size: 12px; }
  .card--back .brand-tagline { font-size: 5.5px; margin-top: 2px; }
</style>
</head>
<body>

<section class="card card--front" aria-label="Business card front">
  <svg class="card-art" width="448" height="272" viewBox="0 0 448 272" aria-hidden="true">
    <rect x="0" y="108" width="7" height="56" fill="var(--teal)"/>
    <rect x="0" y="164" width="7" height="54" fill="var(--lavender-grey)"/>
    <rect x="0" y="218" width="7" height="54" fill="var(--navy)"/>

    <rect x="248" y="0" width="40" height="35" fill="var(--teal-dark)"/>
    <rect x="288" y="0" width="40" height="35" fill="var(--sky)"/>
    <rect x="328" y="0" width="40" height="35" fill="var(--pale)"/>
    <rect x="368" y="0" width="40" height="35" fill="var(--mid-blue)"/>
    <rect x="408" y="0" width="40" height="35" fill="var(--blue)"/>

    <g fill="none" stroke="#fff" stroke-width="1.6" stroke-linejoin="round" stroke-linecap="round">
      <path d="M263 11 l3 -1 l2 4 l-2 2 q2 4 5 6 l2 -2 l4 2 l-1 3 q-8 1 -13 -14 z" fill="#fff"/>
      <rect x="300" y="11" width="14" height="13"/>
      <line x1="303" y1="15" x2="311" y2="15"/>
      <line x1="303" y1="19" x2="311" y2="19"/>
      <rect x="340" y="12" width="16" height="11"/>
      <polyline points="340,12 348,18 356,12"/>
      <path d="M388 26 q-6 -7 -6 -11 a6 6 0 0 1 12 0 q0 4 -6 11 z" fill="#fff" stroke="none"/>
      <circle cx="388" cy="15" r="2" fill="var(--mid-blue)" stroke="none"/>
      <circle cx="428" cy="17.5" r="7"/>
      <ellipse cx="428" cy="17.5" rx="3" ry="7"/>
      <line x1="421" y1="17.5" x2="435" y2="17.5"/>
    </g>

    <g fill="none" stroke="var(--line)" stroke-width="1">
      <polyline points="268,35 268,154"/>
      <polyline points="308,35 308,174 268,174"/>
      <polyline points="348,35 348,193 268,193"/>
      <polyline points="388,35 388,213 268,213"/>
      <polyline points="428,35 428,248 268,248"/>
    </g>
    <circle cx="268" cy="154" r="3.5" fill="var(--teal-dark)"/>
    <circle cx="268" cy="174" r="3.5" fill="var(--sky)"/>
    <circle cx="268" cy="193" r="3.5" fill="var(--pale)"/>
    <circle cx="268" cy="213" r="3.5" fill="var(--mid-blue)"/>
    <circle cx="268" cy="248" r="3.5" fill="var(--blue)"/>
  </svg>

  <div class="brand">
    <span class="brand-dot"></span>
    <div>
      <div class="brand-name">PULSEWISE<br>SYSTEMS</div>
      <span class="brand-tagline">connected to your clinic</span>
    </div>
  </div>

  <div class="holder">
    <p class="holder-name">Full Name</p>
    <p class="holder-title">Function Title</p>
  </div>

  <p class="contact-label" style="top:146px">Phone</p>
  <p class="contact-label" style="top:166px">Fax</p>
  <p class="contact-label" style="top:185px">Email</p>
  <p class="contact-label" style="top:205px">Address lines 1<br>Address lines 2</p>
  <p class="contact-label" style="top:240px">website</p>
</section>

<section class="card card--back" aria-label="Business card back">
  <svg class="card-art" width="448" height="272" viewBox="0 0 448 272" aria-hidden="true">
    <rect x="0" y="0" width="39" height="42" fill="var(--blue)"/>
    <rect x="39" y="0" width="40" height="42" fill="var(--mid-blue)"/>
    <rect x="79" y="0" width="40" height="42" fill="var(--pale)"/>
    <rect x="119" y="0" width="39" height="42" fill="var(--sky)"/>
    <rect x="158" y="0" width="40" height="42" fill="var(--teal)"/>
    <rect x="440" y="163" width="8" height="53" fill="var(--lavender-grey)"/>
    <rect x="440" y="216" width="8" height="56" fill="var(--navy)"/>
  </svg>

  <p class="tagline-band">connected to your clinic</p>

  <div class="brand">
    <span class="brand-dot"></span>
    <div>
      <div class="brand-name">PULSEWISE<br>SYSTEMS</div>
      <span class="brand-tagline">connected to your clinic</span>
    </div>
  </div>
</section>

</body>
</html>
```